Sophisticated, clean website reflecting my feminine, playful side to sell my abstract art,

I need a website no more than 3 pages to showcase my paintings, a little about me and some contact info. I do abstracts so looking for something a little edgy, yet feminine and current.
Updates

Hi there, These are some artists websites that I Iike: Mirabelvoss.com (I like how airy it is) tobiasmerrowind.com kevinplodderas.com (I like how it scrolls) I'll need a place for a photo ( a headshot-i do not have it yet so I'll need to be able to upload that later) as well as an area for my bio. Also, it's important that I will be able to upload any new photos and descriptions easily so it should be user friendly. Lastly, I like in a sunny place so would like to have this seem upbeat and playful as that is how i like to paint. thanks-I'm trying to upload my photos now -

Target Market(s)

ppl ages 35-70 who want large scale art for their homes

Industry/Entity Type

art

Coding

Coded - Design and coding required

Number of Pages Required

3 page

Colors

Designer to choose colors to be used in the design.

Requirements
Must have
• photos of my art, a place for my bio, be easy to reach me. tasteful-nothing too "in your face" -my clients are pretty high end and organized. They like clean lines
Nice to have
• sophisticated background, muted tones in the back-similar clean font throughout-no cursive
Should not have
• too many dark areas. Too many blocks of color. Too serious.

```html
<!DOCTYPE html>
<html lang="en">
<head>
<meta charset="utf-8">
<title>Mara — Visual Designer</title>
<link href="https://fonts.googleapis.com/css2?family=Poppins:wght@300;400;500&display=swap" rel="stylesheet">
<style>
:root{
  --pink:#f18a9b;
  --pink-soft:#f7c3cc;
  --ink:#2f2f3a;
  --muted:#555;
  --line:#d9d9d9;
  --wash:#fdf6f4;
  --cream:#fbf3e6;
  --footer:#f4879a;
  --dark:#444;
}
*{margin:0;padding:0;box-sizing:border-box}
html,body{width:1200px;height:3861px;overflow:hidden}
body{font-family:'Poppins',sans-serif;color:var(--ink);background:#fff;position:relative}
.abs{position:absolute}
section,header,footer{position:absolute;left:0;width:1200px}
/* hero */
.hero{top:0;height:653px;background:
  radial-gradient(ellipse 420px 300px at 80px 420px,rgba(241,138,155,.35),transparent 70%),
  radial-gradient(ellipse 380px 260px at 60px 120px,rgba(241,138,155,.25),transparent 70%),
  radial-gradient(ellipse 500px 300px at 1000px 100px,rgba(240,214,170,.45),transparent 70%),
  radial-gradient(ellipse 500px 260px at 1050px 560px,rgba(240,214,170,.35),transparent 70%),
  #fdf3f0}
.logo{left:115px;top:56px;font-size:19px;color:var(--ink)}
.logo span{color:var(--pink)}
.nav{top:59px;left:518px;display:flex;gap:0;font-size:15px}
.nav a{color:var(--ink);text-decoration:none}
.nav a.active{color:var(--pink)}
.nav .sep{margin:0 19px;color:var(--ink)}
.burger{left:1070px;top:52px;width:46px}
.burger i{display:block;height:2px;background:var(--pink);margin-bottom:10px;margin-left:auto}
.hero-rule{left:0;top:203px;width:95px;height:1px;background:var(--pink)}
.hello{left:115px;top:198px;font-size:19px}
.headline{left:115px;top:252px;font-size:54px;font-weight:400;color:var(--pink);letter-spacing:1px;white-space:nowrap;z-index:2}
.intro{left:115px;top:315px;font-size:20px;line-height:42px;color:var(--muted);width:400px}
.socials{left:105px;top:442px;display:flex;gap:20px}
.socials i{width:46px;height:46px;border-radius:50%;border:1.5px solid var(--pink-soft)}
.socials i.on{background:#2fc6ee;border-color:#2fc6ee}
.rights{left:125px;top:530px;font-size:15px;display:flex;align-items:center;gap:12px}
.rights b{width:14px;height:14px;border-radius:50%;background:var(--pink);display:block}
.rights-rule{left:130px;top:555px;width:85px;height:1px;background:var(--pink)}
.art{background:linear-gradient(135deg,#b79ab0,#e8c3c6,#5a3b45)}
.pager{left:1099px;display:flex;flex-direction:column;gap:22px;top:329px}
.pager i{width:16px;height:16px;border-radius:50%;border:1px solid var(--pink)}
.pager i.on{box-shadow:inset 0 0 0 3px #fff;background:var(--pink)}
.count{left:1090px;top:570px;font-size:14px}
/* about */
.about{top:653px;height:587px;background:var(--wash)}
.eyebrow{font-size:13px;color:var(--pink)}
.eyebrow::before{content:"";display:inline-block;width:18px;height:1px;background:var(--pink);vertical-align:middle;margin-right:6px}
.h2{font-size:22px;line-height:34px;font-weight:400}
.h2 em{font-style:normal;color:var(--pink)}
.small{font-size:14px;line-height:34px;color:var(--ink)}
.mail{font-size:14px;color:#888;display:flex;align-items:center;gap:10px}
.stat{height:63px;width:216px;background:var(--pink);border-radius:4px;color:#fff;display:flex;align-items:center;gap:8px;padding-left:12px;font-size:14px}
.stat b{width:46px;height:46px;border-radius:50%;border:1.5px solid #fff;display:flex;align-items:center;justify-content:center;font-size:19px;font-weight:500}
/* services */
.services{top:1240px;height:445px;background:#fff}
.card{top:88px;width:299px;height:270px;border:1px solid var(--line);border-radius:6px;text-align:center;background:#fff}
.card.featured{background:var(--pink);border-color:var(--pink);color:#fff}
.card .ico{width:78px;height:78px;border-radius:50%;background:var(--pink);margin:42px auto 0;display:flex;align-items:center;justify-content:center}
.card.featured .ico{background:#fff}
.card h3{font-size:28px;font-weight:400;color:var(--pink);margin-top:24px}
.card.featured h3{color:#fff}
.card p{font-size:14px;margin-top:14px}
/* gallery */
.gallery{top:1685px;height:1310px;background:
  radial-gradient(ellipse 500px 200px at 700px 20px,rgba(241,138,155,.12),transparent 70%),#fff}
.g-title{left:118px;top:70px;font-size:30px;color:var(--pink)}
.g-rule{left:118px;top:117px;width:48px;height:2px;background:var(--pink)}
.filters{left:822px;top:82px;font-size:15px;display:flex}
.filters .sep{margin:0 20px}
.filters .on{color:var(--pink)}
.tile{border-radius:3px}
.t-blue{background:linear-gradient(160deg,#4d86c8,#f3efe8 45%,#d4602c)}
.t-violet{background:linear-gradient(135deg,#d6cde0,#6b4f8f,#efe7ea)}
.t-teal{background:linear-gradient(135deg,#3a9aa0,#c8782c,#2c4a3a)}
.t-green{background:linear-gradient(90deg,#8ea0c8,#e8e2d6 35%,#0f8a7c 50%,#e8e2d6 70%,#2a3a6a)}
.t-drip{background:linear-gradient(180deg,#a07846 0 4%,#f0eeea 12%,#7fc0dc 70%,#a07846 96%)}
.t-gold{background:linear-gradient(135deg,#d6b23a,#eef0f2,#2e4a98,#8a6a44)}
.t-rose{background:linear-gradient(135deg,#f2e6e6,#7a3e3a,#e7c3c0)}
.t-brown{background:linear-gradient(135deg,#f3ece8,#5a2418,#e8d5d0)}
.t-purple{background:linear-gradient(135deg,#efe9e2,#4a3ca0,#5a2a3a,#ece6f0)}
/* social */
.social{top:2995px;height:605px;background:
  radial-gradient(ellipse 400px 260px at 150px 80px,rgba(241,138,155,.22),transparent 70%),
  radial-gradient(ellipse 500px 280px at 900px 140px,rgba(240,214,170,.35),transparent 70%),#fdf6f2}
.link-card{width:299px;height:87px;border:1px solid #e4e4e4;border-radius:8px;background:#fff;padding:16px 30px}
.link-card h4{font-size:22px;font-weight:400;color:var(--pink)}
.link-card p{font-size:14px;margin-top:6px}
.link-card .mark{position:absolute;right:28px;top:22px;width:32px;height:32px;border-radius:50%;border:2px solid var(--pink)}
.link-card.featured{background:var(--pink);border-color:var(--pink)}
.link-card.featured h4,.link-card.featured p{color:#fff}
/* footer */
.footer{top:3600px;height:261px;background:var(--footer);color:#fff;text-align:center}
.talk{left:0;width:1186px;top:50px;font-size:22px}
.chat{left:977px;top:53px;width:105px;height:34px;background:var(--dark);border-radius:3px;font-size:12px;display:flex;align-items:center;justify-content:center}
.f-nav{top:135px;font-size:13px;font-weight:500}
.copy{left:0;width:1186px;top:198px;font-size:12px}
</style>
</head>
<body>

<header class="hero">
  <div class="abs logo"><span>Logo</span> Here</div>
  <nav class="abs nav">
    <a class="active" href="#">Home</a><span class="sep">|</span>
    <a href="#">About Us</a><span class="sep">|</span>
    <a href="#">Gallery</a><span class="sep">|</span>
    <a href="#">Blog</a><span class="sep">|</span>
    <a href="#">Contact Us</a>
  </nav>
  <div class="abs burger"><i style="width:46px"></i><i style="width:32px"></i><i style="width:46px"></i></div>
  <div class="abs hero-rule"></div>
  <p class="abs hello">HELLO, I AM MARA</p>
  <h1 class="abs headline">i’M A VISUAL DESIGNER</h1>
  <p class="abs intro">Are you looking for a designer who works hard but stays humble?</p>
  <div class="abs socials"><i></i><i class="on"></i><i></i><i></i></div>
  <div class="abs rights"><b></b>All right reserved.. 2022</div>
  <div class="abs rights-rule"></div>
  <div class="abs art" style="left:518px;top:152px;width:340px;height:416px" role="img" aria-label="Abstract rose painting in pink, mauve and black"></div>
  <div class="abs art" style="left:873px;top:152px;width:164px;height:201px;background:linear-gradient(135deg,#c8962c,#2e4a8a,#d6a040)" role="img" aria-label="Abstract painting in ochre and blue swirls"></div>
  <div class="abs art" style="left:873px;top:368px;width:164px;height:200px;background:linear-gradient(135deg,#3a9aa0,#c8782c,#1f2d24)" role="img" aria-label="Abstract painting with teal and orange bursts"></div>
  <div class="abs pager"><i class="on"></i><i></i><i></i><i></i><i></i></div>
  <div class="abs count">1 | 5</div>
</header>

<section class="about">
  <p class="abs eyebrow" style="left:118px;top:131px">Contact</p>
  <h2 class="abs h2" style="left:118px;top:158px">Any Type Of Query and<br><em>Discussion</em></h2>
  <p class="abs small" style="left:118px;top:238px;width:360px">Sed ut perspicaatis unde omnis iste natus error sit voluptatem accusantium</p>
  <p class="abs mail" style="left:118px;top:323px">hi@maraviel.com
    <svg width="38" height="10" viewBox="0 0 38 10"><path d="M0 5h36M31 1l5 4-5 4" stroke="#f18a9b" fill="none" stroke-width="1.2"/></svg></p>
  <div class="abs stat" style="left:118px;top:375px"><b>25</b>Years of Experienne</div>
  <div class="abs stat" style="left:355px;top:375px"><b>180</b>Satisfied Clients</div>
  <h2 class="abs h2" style="left:630px;top:158px;width:420px">You <em>can't use up creativity</em>, the more you use, more you have in your signifiant mind.</h2>
  <p class="abs small" style="left:630px;top:285px;width:450px;line-height:30px;font-size:13.5px">Sed ut perspicaatis unde omnis iste natus error sit volu ptatem accusantium Sed ut perspicaatis unde omnis iste natus error sit voluptatem accusantium Sed ut perspicaatis unde omnis iste natus error sit&nbsp; voluptatem accusantium Sed ut perspicaatis unde omnis natus error sit voluptatem.</p>
</section>

<section class="services">
  <div class="abs card featured" style="left:118px">
    <div class="ico"><svg width="40" height="40" viewBox="0 0 40 40"><path d="M20 4l15 11-6 18H11L5 15z" fill="none" stroke="#f18a9b" stroke-width="2"/></svg></div>
    <h3>Product Designer</h3><p>124 Projects</p>
  </div>
  <div class="abs card" style="left:452px">
    <div class="ico"><svg width="32" height="32" viewBox="0 0 32 32"><path d="M8 24l4-10 8-6 4 4-6 8z" fill="#fff"/><circle cx="15" cy="17" r="2" fill="#f18a9b"/></svg></div>
    <h3>BrandingDesigner</h3><p>24 Projects</p>
  </div>
  <div class="abs card" style="left:785px">
    <div class="ico"><svg width="40" height="40" viewBox="0 0 40 40"><rect x="6" y="10" width="28" height="18" rx="9" fill="none" stroke="#fff" stroke-width="2.5"/><circle cx="14" cy="28" r="4" fill="#fff"/></svg></div>
    <h3>Ful Stack Developer</h3><p>224 Projects</p>
  </div>
</section>

<section class="gallery">
  <h2 class="abs g-title" style="font-weight:400">My Painting Gallery</h2>
  <div class="abs g-rule"></div>
  <div class="abs filters"><span class="on">All</span><span class="sep">|</span><span>Latest</span><span class="sep">|</span><span>Most Views</span><span class="sep">|</span></div>
  <div class="abs tile t-blue" style="left:118px;top:161px;width:298px;height:514px" role="img" aria-label="Two abstract canvases with blue washes and orange loops"></div>
  <div class="abs tile t-gold" style="left:118px;top:707px;width:298px;height:513px" role="img" aria-label="Canvas with gold and navy flower-like swirls"></div>
  <div class="abs tile t-violet" style="left:445px;top:161px;width:298px;height:236px" role="img" aria-label="Abstract violet splatter blooms on white"></div>
  <div class="abs tile t-green" style="left:445px;top:436px;width:298px;height:236px" role="img" aria-label="Vertical panels in slate blue, white and teal"></div>
  <div class="abs tile t-rose" style="left:445px;top:711px;width:298px;height:236px" role="img" aria-label="Brown and blush abstract roses"></div>
  <div class="abs tile t-brown" style="left:445px;top:985px;width:298px;height:235px" role="img" aria-label="Dark brown abstract leaf shapes on white"></div>
  <div class="abs tile t-teal" style="left:771px;top:161px;width:299px;height:330px" role="img" aria-label="Explosive teal and orange abstract painting"></div>
  <div class="abs tile t-drip" style="left:771px;top:526px;width:299px;height:330px" role="img" aria-label="White canvas with light blue drips on wood"></div>
  <div class="abs tile t-purple" style="left:771px;top:891px;width:299px;height:329px" role="img" aria-label="Purple and plum abstract burst"></div>
</section>

<section class="social">
  <p class="abs" style="left:118px;top:112px;font-size:13px;color:var(--pink)">Social Media</p>
  <h2 class="abs" style="left:118px;top:145px;font-size:22px;font-weight:500;letter-spacing:1px">Let’s&nbsp; Be&nbsp; Freinds</h2>
  <div class="abs link-card" style="left:118px;top:247px"><h4>Workline</h4><p>Professional Social Profile</p><span class="mark" style="border-radius:3px"></span></div>
  <div class="abs link-card" style="left:449px;top:247px"><h4>Shotboard</h4><p>Design work Social Profile</p><span class="mark"></span></div>
  <div class="abs link-card" style="left:781px;top:247px"><h4>Picframe</h4><p>Image base social communications</p><span class="mark" style="border-radius:8px"></span></div>
  <div class="abs link-card" style="left:118px;top:361px"><h4>Chirpnote</h4><p>Random thoughts</p><span class="mark"></span></div>
  <div class="abs link-card" style="left:449px;top:361px"><h4>Longread</h4><p>Work case Study</p><span class="mark"></span></div>
  <div class="abs link-card featured" style="left:781px;top:361px"><h4>Emial</h4><p>hello@maraviel.studio</p>
    <svg style="position:absolute;right:26px;top:28px" width="32" height="24" viewBox="0 0 32 24"><rect x="1" y="1" width="30" height="22" rx="2" fill="none" stroke="#fff" stroke-width="1.5"/><path d="M1 2l15 11L31 2" fill="none" stroke="#fff" stroke-width="1.5"/></svg></div>
</section>

<footer class="footer">
  <p class="abs talk">Let’s&nbsp; Talk?</p>
  <div class="abs chat">LET'S CHAT</div>
  <span class="abs f-nav" style="left:312px">ABOUT</span>
  <span class="abs f-nav" style="left:424px">WORKS</span>
  <span class="abs f-nav" style="left:540px">CASE&nbsp; STUDY</span>
  <span class="abs f-nav" style="left:693px">CLIENTS</span>
  <span class="abs f-nav" style="left:813px">CONTACT</span>
  <p class="abs copy">ALL RIGHT RESERVED 2022</p>
</footer>

</body>
</html>
```